Glossy black background with white text, image of webcam on right.

Text:

YOU HAVE BEEN CHOSEN
to be a Camgirl online model!

- earn $10,000/month from home
- choose your own hours

Solara Finch
The Halvern

Desmond Pryke
Director
VELTRIXO PTY LTD
mob 0491 203884
email sales@veltrixo.com

www.VELTRIXO.com

the Finch signature can go on the back.

Solara Finch
The Halvern

thanks

On the front: the webcam image should be quite large

On the back: Finch sig with an apple image or icon

good luck!

On the back should be in cursive with a small apple picture. (green)

Finch
The Halvern

no "solara"

young hot women

• "You Have Been Chosen"
in the largest font
• see attached photo of webcam
maybe some yellow text
• consider removing logo from webcam pic

```html
<!DOCTYPE html>
<html lang="en">
<head>
<meta charset="utf-8">
<title>Desmond Pryke – VELTRIXO PTY LTD</title>
<link rel="stylesheet" href="https://fonts.googleapis.com/css2?family=Righteous&family=Lobster&family=Sansita:ital,wght@0,800;1,800&display=swap">
<style>
  :root {
    --ink: #000000;
    --paper: #ffffff;
    --signal-red: #c8242b;
    --band-red: #b3151c;
    --cam-light: #e9e9e9;
    --cam-mid: #9c9c9c;
    --cam-dark: #2a2a2a;
  }
  html, body {
    margin: 0;
    padding: 0;
    width: 1200px;
    height: 720px;
    overflow: hidden;
    background: var(--ink);
  }
  .card {
    position: relative;
    width: 1200px;
    height: 720px;
    overflow: hidden;
    background: var(--ink);
  }
  .webcam-photo {
    position: absolute;
    left: 0;
    top: 0;
    width: 1200px;
    height: 720px;
  }
  .headline-band {
    position: absolute;
    left: 84px;
    top: 86px;
    width: 860px;
    height: 112px;
  }
  .headline {
    position: absolute;
    left: 92px;
    top: 96px;
    margin: 0;
    font-family: "Righteous", sans-serif;
    font-weight: 400;
    font-size: 66px;
    letter-spacing: 1px;
    line-height: 1;
    color: var(--ink);
    -webkit-text-stroke: 1.5px #5a5a5a;
    white-space: nowrap;
  }
  .subhead {
    position: absolute;
    left: 138px;
    top: 230px;
    margin: 0;
    font-family: "Lobster", cursive;
    font-size: 40px;
    line-height: 1;
    color: var(--signal-red);
    white-space: nowrap;
  }
  .perks {
    position: absolute;
    left: 203px;
    top: 340px;
    margin: 0;
    padding: 0;
    list-style: none;
    font-family: "Lobster", cursive;
    font-size: 22px;
    line-height: 31px;
    color: var(--signal-red);
  }
  .contact {
    position: absolute;
    left: 92px;
    top: 480px;
    margin: 0;
    font-family: "Sansita", sans-serif;
    font-style: italic;
    font-weight: 800;
    font-size: 22px;
    line-height: 31.5px;
    color: var(--paper);
    letter-spacing: 0.5px;
  }
  .contact span { display: block; }
  .brand-mark {
    position: absolute;
    left: 704px;
    top: 524px;
    margin: 0;
    font-family: "Sansita", sans-serif;
    font-weight: 800;
    color: var(--signal-red);
    line-height: 1;
  }
  .brand-mark .prefix { display: block; font-size: 28px; }
  .brand-mark .name { display: block; font-size: 62px; letter-spacing: 1px; margin-top: -4px; }
  .brand-mark .suffix { display: block; font-size: 28px; text-align: right; margin-top: -6px; }
</style>
</head>
<body>
<main class="card">
  <svg class="webcam-photo" viewBox="0 0 1200 720" role="img" aria-label="Black and white photograph of a large white webcam with a ribbed dark lens, filling the right side of the card">
    <defs>
      <radialGradient id="cam-body" cx="880" cy="360" r="520" gradientUnits="userSpaceOnUse">
        <stop offset="0" stop-color="var(--cam-dark)"/>
        <stop offset="0.3" stop-color="var(--cam-mid)"/>
        <stop offset="0.55" stop-color="var(--cam-light)"/>
        <stop offset="0.8" stop-color="#cfcfcf"/>
        <stop offset="1" stop-color="var(--ink)" stop-opacity="0"/>
      </radialGradient>
    </defs>
    <rect x="380" y="0" width="820" height="720" fill="url(#cam-body)"/>
  </svg>

  <svg class="headline-band" viewBox="0 0 860 112" aria-hidden="true">
    <defs>
      <linearGradient id="band-fade" x1="0" y1="0" x2="1" y2="0">
        <stop offset="0" stop-color="var(--band-red)" stop-opacity="0.85"/>
        <stop offset="0.5" stop-color="var(--band-red)"/>
        <stop offset="1" stop-color="var(--band-red)" stop-opacity="0.9"/>
      </linearGradient>
    </defs>
    <path d="M4 14 L300 6 L620 10 L856 2 L848 96 L560 106 L260 100 L0 108 Z" fill="url(#band-fade)"/>
  </svg>

  <h1 class="headline">YOU HAVE BEEN CHOSEN</h1>
  <p class="subhead">to be a Camgirl online model!</p>

  <ul class="perks">
    <li>-earn $10,000/month from home</li>
    <li>-choose your own hours</li>
  </ul>

  <address class="contact">
    <span class="contact-name">Desmond Pryke</span>
    <span class="contact-role">Director</span>
    <span class="contact-company">VELTRIXO PTY LTD</span>
    <span class="contact-phone">mob 0491 203884</span>
    <span class="contact-email">email sales@veltrixo.com</span>
  </address>

  <p class="brand-mark">
    <span class="prefix">www.</span>
    <span class="name">VELTRIXO</span>
    <span class="suffix">.com</span>
  </p>
</main>
</body>
</html>
```